Game like design for my android application

Please take a look at Lumora Staff fundhatch campaign over here: https://www.fundhatch.example/projects/lumorastaff/4820193756/

I need to have a design done for the app. I am not really good in designing stuff as you can see on our fundhatch page. Therefore I don't know whether it should have an antic look or a modern look or a combination of these two.

I would suggest it might have a look similar to the attached file.

But I have no idea and thus I would expect you to come up with ideas. The app is a game-like which involves experience points, achievements, items, battles, medals maybe and such. So I would welcome some knowledge of these kind of things.

Great would be if it could have this Tobin Quell-like look.

Please see this mockup https://sketchvale.example/s/Q2RKD. I just made (please don't stick to that, it should just give you an idea of the application lifecycle, but come up with your own ideas of how those elements should be positioned, how should they look and so on).

Plus see attached logo, maybe the app should keep such color scale.

Hey guys, just a note. Please do not stick to my mock up very much, especially not to the main menu. That menu is there only to display what elements should it have, but I would be happy to see some original user friendly ideas of how that menu could be done. Besides that, thanks a lot for your designs, they look awesome, keep the great work! :)

Games

• Antic-modern gaming look

```html
<!DOCTYPE html>
<html lang="en">
<head>
<meta charset="utf-8">
<title>Lumora Staff – Player Profile</title>
<link href="https://fonts.googleapis.com/css2?family=EB+Garamond:wght@400;500;600&display=swap" rel="stylesheet">
<style>
  :root {
    --bg-top: #0f2233;
    --bg-bottom: #0b1a28;
    --panel: #0a1622;
    --gold: #c9a55c;
    --gold-soft: #b8975a;
    --gold-light: #e2c98f;
    --cream: #ece3cf;
    --health: #c0392f;
    --mana: #3b3db3;
    --bar-empty: #0a0a0a;
    --link: #2fd0e6;
    --toggle-off: #b89a52;
    --toggle-on: #1d6a1d;
    --toggle-off-text: #2a2114;
    --toggle-on-text: #d8c48a;
  }
  html, body {
    margin: 0;
    padding: 0;
    overflow: hidden;
  }
  body {
    width: 675px;
    height: 1200px;
    background: var(--bg-bottom);
  }
  .profile-screen {
    position: relative;
    width: 675px;
    height: 1200px;
    overflow: hidden;
    background: linear-gradient(180deg, var(--bg-top) 0%, var(--bg-bottom) 100%);
    font-family: "EB Garamond", Georgia, serif;
    color: var(--gold);
  }
  .brand-emblem {
    position: absolute;
    left: 74px;
    top: 74px;
    width: 212px;
    height: 212px;
    border-radius: 50%;
    background: #050505;
    border: 3px solid var(--gold);
    box-sizing: border-box;
    display: flex;
    align-items: center;
    justify-content: center;
    text-align: center;
  }
  .brand-name {
    font-size: 36px;
    font-weight: 500;
    line-height: 1.05;
    color: var(--gold);
  }
  .username {
    position: absolute;
    left: 314px;
    top: 82px;
    margin: 0;
    font-size: 42px;
    font-weight: 500;
    letter-spacing: 1px;
    color: var(--cream);
  }
  .stat-bar {
    position: absolute;
    left: 317px;
    width: 342px;
    height: 29px;
    box-sizing: border-box;
    border: 2px solid var(--gold);
    background: var(--bar-empty);
  }
  .stat-bar .fill {
    height: 100%;
  }
  .stat-bar.health { top: 153px; }
  .stat-bar.health .fill { width: 74%; background: var(--health); }
  .stat-bar.mana { top: 205px; }
  .stat-bar.mana .fill { width: 74%; background: var(--mana); }
  .player-level,
  .player-wins,
  .favourite-spell {
    position: absolute;
    margin: 0;
    font-size: 28px;
    color: var(--gold);
  }
  .player-level { left: 74px; top: 318px; }
  .player-wins { left: 442px; top: 304px; }
  .favourite-spell { left: 74px; top: 390px; }
  .favourite-spell .spell-name {
    color: var(--link);
    text-decoration: underline;
  }
  .battle-mode {
    position: absolute;
    left: 0;
    top: 500px;
    width: 675px;
  }
  .battle-mode-label {
    margin: 0 0 20px 0;
    padding-left: 30px;
    text-align: center;
    font-size: 28px;
    color: var(--gold);
  }
  .battle-toggle {
    display: flex;
    width: 342px;
    height: 79px;
    margin-left: 164px;
  }
  .battle-toggle span {
    flex: 1;
    display: flex;
    align-items: center;
    justify-content: center;
    font-size: 44px;
    letter-spacing: 2px;
  }
  .battle-toggle .off { background: var(--toggle-off); color: var(--toggle-off-text); }
  .battle-toggle .on { background: var(--toggle-on); color: var(--toggle-on-text); }
  .main-menu {
    position: absolute;
    left: 40px;
    top: 680px;
    width: 592px;
    height: 492px;
    background: var(--panel);
    box-shadow: 0 0 30px rgba(0, 0, 0, 0.35);
  }
  .main-menu ul {
    list-style: none;
    margin: 0;
    padding: 28px 0 0 0;
  }
  .main-menu li {
    position: relative;
    height: 86px;
    display: flex;
    align-items: center;
    justify-content: center;
    font-size: 38px;
    letter-spacing: 2px;
    color: var(--gold-soft);
  }
  .main-menu li + li::before {
    content: "";
    position: absolute;
    top: 0;
    left: 74px;
    right: 74px;
    height: 2px;
    background: linear-gradient(90deg, transparent, rgba(201, 165, 92, 0.55), transparent);
  }
</style>
</head>
<body>
  <main class="profile-screen">
    <div class="brand-emblem">
      <span class="brand-name">Lumora<br>Staff</span>
    </div>

    <h1 class="username">Username</h1>
    <div class="stat-bar health" aria-label="Health"><div class="fill"></div></div>
    <div class="stat-bar mana" aria-label="Mana"><div class="fill"></div></div>

    <p class="player-wins">Wins : 10</p>
    <p class="player-level">Beginner : I lvl.</p>
    <p class="favourite-spell">Most used spell: <span class="spell-name">Ventusio</span></p>

    <section class="battle-mode">
      <p class="battle-mode-label">Battle mode:</p>
      <div class="battle-toggle">
        <span class="off">OFF</span>
        <span class="on">ON</span>
      </div>
    </section>

    <nav class="main-menu">
      <ul>
        <li>SPELLBOOK</li>
        <li>STATS</li>
        <li>RANKING</li>
        <li>INVENTORY</li>
        <li>MATCH HISTORY</li>
      </ul>
    </nav>
  </main>
</body>
</html>
```